Redesigning of the packaging for 4 GOLDEN HEARTH gourmet breads

We need new designs for our range of four gourmet sliced breads, called GOLDEN HEARTH. These breads are prepared with specially selected ingredients sourced from several countries and with extreme focus on quality, health and indulgent pleasure. The Golden Hearth brand aims to solve the boring and bland nature of white breads and comes in several flavours such as coconut, seeds & nuts, exotic fruits and vegetables, buttermilk, chocolate, etc.
The Golden Hearth brand positioning statement is JOY IN EVERY SLICE
The current packaging designs are still quite attractive which makes it a difficult decision, but we know it's time for a rebrand, and therefore we really want the best possible designs - ONLY THE BEST!
GOLDEN HEARTH currently comprises three 'sister' products and one new addition named as follows:
1. Golden Hearth - buttermilk dream (yellow color)
2. Golden Hearth - cocoa swirl (brown & orange color)
3. Golden Hearth - tropic coconut (green & cream color)
4. Hearth Tots - (kiddies' style - This is a kiddies bread)
[Some pictures of the current packaging are attached, alongside with the content, layout and dimensions which should be used for the new designs, including ingredients, addresses, etc. Check the file 'Back view with ingredients and contents.pdf'; 'Layout and Dimensions of current Golden Hearth Packaging.pdf]
5. The logo may or may not be modified. (Golden Hearth Logo.pdf)
Key points to note:
- Demographic: The target audience is mainly young and middle aged from the middle to upper economic class
- Psychographic: Health conscious, Class conscious, Family focused consumers, Environment and Sustainable development minded consumers
- The designs will be similar in style for the 3 variants but be differentiated by colours and content
- The fonts and the overall design should be modern, playful and inviting.
- The content of the packaging is in the attachments
- Total designs - 4 designs.
Target Market(s)
The target market is kids, teens, young adults. Middle to upper economic class. Premium segment, lifestyle conscious consumers.
Industry/Entity Type
Bakery
Colors
Designer to choose colors to be used in the design.
Look and feel

```html
<!DOCTYPE html>
<html lang="en">
<head>
<meta charset="utf-8">
<title>Golden Hearth – Bread Range</title>
<link href="https://fonts.googleapis.com/css2?family=Oswald:wght@700&family=Montserrat:wght@500;600&display=swap" rel="stylesheet">
<style>
  :root{
    --bg:#e6e6e7;
    --brand-red:#c4161c;
    --ink:#1d1d1d;
    --tie:#1c1c1c;
    --bread-light:#e0a46a;
    --bread-mid:#c97a3f;
    --bread-dark:#9c5428;
    --choco:#e8762d;
    --choco-deep:#b9561e;
    --choco-seal:#b87a5a;
    --coco:#a3cd78;
    --coco-cream:#f4f1d8;
    --butter:#f6e547;
    --butter-deep:#f2d43a;
    --kids:#262626;
    --kids-label:#e9c84a;
    --kids-face:#e4575a;
  }
  *{box-sizing:border-box;margin:0;padding:0}
  html,body{width:1200px;height:995px;overflow:hidden;background:var(--bg)}
  .canvas{position:relative;width:1200px;height:995px;font-family:"Montserrat",sans-serif}

  .brand-mark{position:absolute;left:0;top:50px;width:1200px;text-align:center;
    font-family:"Oswald",sans-serif;font-weight:700;color:var(--brand-red);font-size:62px;line-height:.98}

  .bag{position:absolute;top:253px;width:234px;height:680px}
  .bag-gather{position:absolute;left:10px;top:0;width:214px;height:142px;clip-path:polygon(0 20%,50% 0,100% 12%,66% 100%,34% 100%)}
  .bag-tie{position:absolute;left:87px;top:134px;width:60px;height:16px;background:var(--tie);border-radius:3px}
  .bag-body{position:absolute;left:0;top:148px;width:234px;height:532px;border-radius:30px 30px 18px 18px;overflow:hidden}
  .bread-photo{position:absolute;inset:0;background:linear-gradient(90deg,var(--bread-dark),var(--bread-mid) 20%,var(--bread-light) 50%,var(--bread-mid) 80%,var(--bread-dark))}
  .flavour-band{position:absolute;left:0;right:0;top:178px;bottom:0;opacity:.92}
  .seal{position:absolute;left:41px;top:102px;width:152px;height:152px;border-radius:50%;display:flex;align-items:center;justify-content:center;text-align:center}
  .seal-name{font-family:"Oswald",sans-serif;font-weight:700;color:var(--brand-red);font-size:22px;line-height:1}
  .flavour-frame{position:absolute;left:55px;top:254px;width:124px;height:200px;border:3px solid;border-top:none;display:flex;flex-direction:column;align-items:center;padding-top:36px}
  .slogan{font-family:"Oswald",sans-serif;font-weight:700;text-transform:uppercase;text-align:center;line-height:.95}
  .slogan .s1{font-size:20px;display:block}
  .slogan .s2{font-size:34px;display:block}
  .slogan-rule{width:100px;height:2px;margin:6px 0 8px}
  .flavour{font-size:11px;font-weight:500;letter-spacing:2px;text-align:center;line-height:1.3;text-transform:uppercase}

  .bag-choco{left:76px}
  .bag-choco .bag-gather,.bag-choco .flavour-band{background:var(--choco)}
  .bag-choco .seal{background:var(--choco-seal);border:3px solid var(--choco)}
  .bag-choco .flavour-frame{background:var(--choco);border-color:var(--choco-deep)}
  .bag-choco .slogan,.bag-choco .flavour{color:var(--choco-deep)}
  .bag-choco .slogan-rule{background:var(--choco-deep)}

  .bag-coco{left:341px}
  .bag-coco .bag-gather,.bag-coco .flavour-band{background:var(--coco)}
  .bag-coco .seal{background:var(--coco);border:3px solid var(--coco-cream)}
  .bag-coco .flavour-frame{background:var(--coco-cream);border-color:var(--coco)}
  .bag-coco .slogan,.bag-coco .flavour{color:var(--coco)}
  .bag-coco .slogan-rule{background:var(--coco)}

  .bag-butter{left:619px}
  .bag-butter .bag-gather,.bag-butter .flavour-band{background:var(--butter)}
  .bag-butter .seal{background:var(--butter);border:3px solid var(--butter-deep)}
  .bag-butter .flavour-frame{background:var(--butter-deep);border-color:var(--butter)}
  .bag-butter .slogan,.bag-butter .flavour{color:#fff}
  .bag-butter .slogan-rule{background:#fff}

  .bag-kids{left:889px;width:244px}
  .bag-kids .bag-gather{background:var(--kids);width:224px}
  .bag-kids .bag-tie{left:92px}
  .bag-kids .bag-body{width:244px;background:var(--kids)}
  .kids-bread{position:absolute;left:22px;right:22px;top:330px;bottom:28px;background:linear-gradient(180deg,var(--bread-light),var(--bread-mid))}
  .kids-label{position:absolute;top:116px;width:100%;font-size:12px;font-weight:600;letter-spacing:3px;color:var(--kids-label);text-align:center}
  .kids-name{position:absolute;top:140px;width:100%;text-align:center;font-family:"Oswald",sans-serif;font-weight:700;color:var(--brand-red);font-size:26px;line-height:1}
  .kids-character{position:absolute;left:26px;top:200px;width:192px;height:200px;background:var(--kids-face);border-radius:40px 40px 20px 20px}
</style>
</head>
<body>
<main class="canvas">
  <header class="brand-mark">GOLDEN<br>HEARTH</header>

  <section class="bag bag-choco">
    <div class="bag-gather"></div><div class="bag-tie"></div>
    <div class="bag-body">
      <div class="bread-photo" role="img" aria-label="Sliced bread loaf seen through the bag"></div>
      <div class="flavour-band"></div>
      <div class="flavour-frame">
        <p class="slogan"><span class="s1">Joy in every</span><span class="s2">Slice</span></p>
        <div class="slogan-rule"></div>
        <p class="flavour">Cocoa<br>Swirl</p>
      </div>
      <div class="seal"><span class="seal-name">GOLDEN<br>HEARTH</span></div>
    </div>
  </section>

  <section class="bag bag-coco">
    <div class="bag-gather"></div><div class="bag-tie"></div>
    <div class="bag-body">
      <div class="bread-photo" role="img" aria-label="Sliced bread loaf seen through the bag"></div>
      <div class="flavour-band"></div>
      <div class="flavour-frame">
        <p class="slogan"><span class="s1">Joy in every</span><span class="s2">Slice</span></p>
        <div class="slogan-rule"></div>
        <p class="flavour">Tropic<br>Coconut</p>
      </div>
      <div class="seal"><span class="seal-name">GOLDEN<br>HEARTH</span></div>
    </div>
  </section>

  <section class="bag bag-butter">
    <div class="bag-gather"></div><div class="bag-tie"></div>
    <div class="bag-body">
      <div class="bread-photo" role="img" aria-label="Sliced bread loaf seen through the bag"></div>
      <div class="flavour-band"></div>
      <div class="flavour-frame">
        <p class="slogan"><span class="s1">Joy in every</span><span class="s2">Slice</span></p>
        <div class="slogan-rule"></div>
        <p class="flavour">Buttermilk<br>Dream</p>
      </div>
      <div class="seal"><span class="seal-name">GOLDEN<br>HEARTH</span></div>
    </div>
  </section>

  <section class="bag bag-kids">
    <div class="bag-gather"></div><div class="bag-tie"></div>
    <div class="bag-body">
      <div class="kids-bread" role="img" aria-label="Sliced bread visible through a window in the bag"></div>
      <p class="kids-label">KIDDIES BREAD</p>
      <p class="kids-name">HEARTH TOTS</p>
      <div class="kids-character" role="img" aria-label="Playful red cartoon creature mascot"></div>
    </div>
  </section>
</main>
</body>
</html>
```